Flyer for Beacon Ledger & Returns, a local tax practice

Flyer for my business to be distributed locally in the Western Suburb of Melbourne (Size: DL, Fold: Flat, Backside: Blank) This will include below information (Font, color and capitalization of the text is for the designer's creativity):
Beacon Ledger & Returns Your Local Tax Accountant
ABN: 71 284 519 036
Address: 9 Mirra Close, Tarwin Heights
dovpelk@blrau.com.au
Call Florin on 0417 865 209 to book your appointment
Services we offer:
Individual & Company Tax Returns
Company & Trust formation
Business Advisory
Bookkeeping
BAS & IAS
Payroll
TPAR
Please include the logo of the business attached which was designed by ArtHarbor few years ago.
Please include the QNE, WRD and Pulva logos somewhere in the bottom, preferable the same size and aligned (attached)

```html
<!DOCTYPE html>
<html lang="en">
<head>
<meta charset="utf-8">
<title>Beacon Ledger &amp; Returns — DL Flyer</title>
<link href="https://fonts.googleapis.com/css2?family=Montserrat:wght@700;800&family=Poppins:wght@400;500;600;700&display=swap" rel="stylesheet">
<style>
  :root {
    --orange: #e8733a;
    --dark: #333333;
    --ink: #1d1d1d;
    --white: #ffffff;
    --panel: #eeeeee;
    --panel-line: #cfcfcf;
    --stage: #e2e2e2;
    --photo-a: #dfe6ee;
    --photo-b: #8d9db0;
  }
  * { margin: 0; padding: 0; box-sizing: border-box; }
  html, body { width: 800px; height: 1200px; overflow: hidden; background: var(--stage); }
  body { position: relative; font-family: "Poppins", sans-serif; }

  .flyer {
    position: absolute; left: 120px; top: 5px;
    width: 586px; height: 1245px;
    transform: scale(0.956); transform-origin: top left;
    background: var(--white); overflow: hidden;
  }
  .flyer-shapes { position: absolute; inset: 0; }

  .brand {
    position: absolute; left: 148px; top: 58px;
    display: flex; align-items: center; gap: 14px;
  }
  .brand-mark { width: 58px; height: 58px; background: var(--white); }
  .brand-name {
    font-family: "Poppins", sans-serif; font-weight: 600;
    font-size: 27px; line-height: 1.1; color: var(--white); width: 220px;
  }

  .headline { position: absolute; left: 0; right: 0; top: 584px; text-align: center; }
  .headline-main {
    font-family: "Montserrat", sans-serif; font-weight: 800;
    font-size: 76px; line-height: 1; color: var(--orange); letter-spacing: 1px;
  }
  .headline-sub {
    font-family: "Montserrat", sans-serif; font-weight: 800;
    font-size: 33px; line-height: 1; color: var(--ink); margin-top: 6px; letter-spacing: 0.5px;
  }
  .headline-sub .amp { font-weight: 500; }
  .tagline { font-size: 30px; color: var(--ink); line-height: 1.1; margin-top: 2px; }

  .divider { position: absolute; left: 40px; top: 747px; width: 506px; height: 1px; background: #9a9a9a; }
  .divider-accent { position: absolute; left: 251px; top: 745px; width: 84px; height: 5px; border-radius: 3px; background: var(--orange); }

  .services {
    position: absolute; left: 40px; top: 790px; width: 507px; height: 173px;
    background: var(--panel); border: 1px solid var(--panel-line); border-radius: 16px;
  }
  .services-tab {
    position: absolute; left: 115px; top: 770px; width: 356px; height: 54px;
  }
  .services-title {
    position: absolute; left: 0; right: 0; top: 781px; text-align: center;
    font-weight: 700; font-size: 22px; line-height: 33px; color: var(--white); letter-spacing: 0.3px;
  }
  .service-list { position: absolute; list-style: none; }
  .service-list li {
    position: relative; padding-left: 16px;
    font-weight: 700; font-size: 14.5px; line-height: 1.15; color: var(--ink);
  }
  .service-list li::before {
    content: ""; position: absolute; left: 0; top: 5px;
    width: 9px; height: 9px; border-radius: 50%; background: var(--orange);
  }
  .service-list--left { left: 80px; top: 843px; }
  .service-list--left li { margin-bottom: 14px; }
  .service-list--right { left: 356px; top: 843px; }
  .service-list--right li { margin-bottom: 10px; }

  .partner-badge { position: absolute; }
  .badge-board { left: 122px; top: 980px; width: 56px; height: 56px; border-radius: 50%; background: #d9d9d9; border: 3px solid #9cbf2e; }
  .badge-institute { left: 210px; top: 980px; width: 116px; height: 50px; border-radius: 8px; background: #d9dbe8; }
  .badge-software { left: 348px; top: 985px; width: 56px; height: 56px; border-radius: 50%; background: #19b5e6; }
  .badge-partner { left: 408px; top: 985px; width: 56px; height: 56px; border-radius: 50%; background: #1a8bb0; }

  .contact-box {
    position: absolute; left: 40px; top: 1070px; width: 506px; height: 90px;
    border: 1.5px solid #9a9a9a; border-radius: 16px;
  }
  .abn {
    position: absolute; left: 168px; top: 1056px; width: 250px; height: 32px;
    border-radius: 16px; background: var(--orange); color: var(--white);
    font-weight: 500; font-size: 19px; line-height: 32px; text-align: center;
    box-shadow: 0 0 0 6px var(--white);
  }
  .contact-line {
    position: absolute; left: 0; right: 0; top: 1100px;
    display: flex; justify-content: center; gap: 14px;
    font-size: 14.5px; color: var(--ink);
  }
  .contact-line span { display: inline-flex; align-items: center; gap: 4px; }

  .cta-band { position: absolute; left: 0; top: 1135px; width: 586px; height: 110px; background: var(--dark); }
  .cta-tab { position: absolute; left: 163px; top: 1135px; width: 260px; height: 34px; }
  .cta-label {
    position: absolute; left: 0; right: 0; top: 1138px; text-align: center;
    font-size: 20px; color: var(--white); letter-spacing: 0.3px;
  }
  .cta-label strong { font-weight: 700; }
  .cta-phone {
    position: absolute; left: 106px; top: 1174px;
    display: flex; align-items: center; gap: 8px; color: var(--white);
  }
  .cta-number { font-weight: 700; font-size: 38px; letter-spacing: 0.5px; }
  .cta-note { font-size: 14px; line-height: 1.15; }
  .cta-note em { font-style: normal; color: var(--orange); display: block; }
</style>
</head>
<body>
<main class="flyer">
  <svg class="flyer-shapes" viewBox="0 0 586 1245" width="586" height="1245" aria-hidden="true">
    <defs>
      <linearGradient id="photoTone" x1="0" y1="0" x2="1" y2="1">
        <stop offset="0" stop-color="var(--photo-a)"/>
        <stop offset="1" stop-color="var(--photo-b)"/>
      </linearGradient>
    </defs>
    <polygon points="0,0 586,0 586,355 293,562 0,360" fill="var(--dark)"/>
    <polygon points="0,378 293,570 0,432" fill="var(--orange)"/>
    <polygon points="586,372 293,570 586,426" fill="var(--orange)"/>
  </svg>

  <div class="brand">
    <span class="brand-mark"></span>
    <span class="brand-name">Beacon Ledger &amp; Returns</span>
  </div>

  <svg class="flyer-shapes" viewBox="0 0 586 1245" width="586" height="1245">
    <polygon role="img" aria-label="Photo of business people reviewing financial charts at a desk"
             points="293,135 528,350 293,568 58,350" fill="url(#photoTone)"
             stroke="var(--white)" stroke-width="3"/>
  </svg>

  <header class="headline">
    <div class="headline-main">BEACON</div>
    <div class="headline-sub">LEDGER <span class="amp">&amp;</span> RETURNS</div>
    <div class="tagline">Your Local Tax Accountant</div>
  </header>
  <div class="divider"></div>
  <div class="divider-accent"></div>

  <section class="services" aria-label="Services we offer"></section>
  <svg class="services-tab" viewBox="0 0 356 54" aria-hidden="true">
    <path d="M0 22 C4 6 14 0 30 0 L326 0 C342 0 352 6 356 22 L326 22 L318 44 C314 52 308 54 300 54 L56 54 C48 54 42 52 38 44 L30 22 Z" fill="var(--dark)"/>
  </svg>
  <div class="services-title">SERVICES WE OFFER</div>
  <ul class="service-list service-list--left">
    <li>Individual &amp; Company<br>Tax Returns</li>
    <li>Company &amp; Trust formation</li>
    <li>Business Advisory</li>
  </ul>
  <ul class="service-list service-list--right">
    <li>Bookkeeping</li>
    <li>BAS &amp; IAS</li>
    <li>Payroll</li>
    <li>TPAR</li>
  </ul>

  <div class="partner-badge badge-board" role="img" aria-label="Registered tax agent badge"></div>
  <div class="partner-badge badge-institute" role="img" aria-label="Accounting institute membership badge"></div>
  <div class="partner-badge badge-software" role="img" aria-label="Accounting software badge"></div>
  <div class="partner-badge badge-partner" role="img" aria-label="Software partner badge"></div>

  <div class="contact-box"></div>
  <div class="abn">ABN: 71 284 519 036</div>
  <div class="contact-line">
    <span>
      <svg width="11" height="14" viewBox="0 0 11 14" aria-hidden="true"><path d="M5.5 0A5.5 5.5 0 0 0 0 5.5C0 9.5 5.5 14 5.5 14S11 9.5 11 5.5A5.5 5.5 0 0 0 5.5 0Z" fill="var(--orange)"/><circle cx="5.5" cy="5.3" r="2" fill="var(--white)"/></svg>
      9 Mirra Close, Tarwin Heights
    </span>
    <span>
      <svg width="14" height="10" viewBox="0 0 14 10" aria-hidden="true"><rect width="14" height="10" rx="1" fill="var(--orange)"/><path d="M0.8 1 7 5.8 13.2 1" stroke="var(--white)" stroke-width="1.2" fill="none"/></svg>
      dovpelk@blrau.com.au
    </span>
  </div>

  <div class="cta-band"></div>
  <svg class="cta-tab" viewBox="0 0 260 34" aria-hidden="true">
    <polygon points="0,0 260,0 240,34 20,34" fill="var(--orange)"/>
  </svg>
  <div class="cta-label"><strong>CALL FLORIN</strong> ON</div>
  <div class="cta-phone">
    <svg width="32" height="32" viewBox="0 0 32 32" aria-hidden="true">
      <circle cx="16" cy="16" r="16" fill="var(--orange)"/>
      <path d="M11 9c1-.6 2-.3 2.5.6l1.3 2.3c.4.8.2 1.6-.5 2.1l-1 .7c.8 1.8 2.2 3.3 4 4.1l.7-1c.5-.7 1.4-.9 2.1-.5l2.3 1.3c.9.5 1.2 1.6.6 2.5l-.8 1.2c-.6.9-1.8 1.3-2.8.9C14.6 21.7 10.3 17.4 8.8 12.6c-.3-1 .1-2.2 1-2.8Z" fill="var(--white)"/>
    </svg>
    <span class="cta-number">0417 865 209</span>
    <span class="cta-note">to book your<em>APPOINTMENT</em></span>
  </div>
</main>
</body>
</html>
```